Professional/modern business card design for construction company

We need a new business card design, double sided keeping it modern, sleek, professional and simple. We are an earthmoving business but do not want any pictures of machinery. I would like one side to have the logo and the other to have all the information, keeping with the colors in our logo. The business card will need to be able to be customised so we can use it for several different managers., we would also like to be able to use the design to apply it to other stationary ie. letterheads, notebooks etc. We do not really have a tag line but we could put on there that we specialise in - Agriculture, Civil Construction and Mining.

Contact Information for Business Card

Brolga Ridge Excavations Pty Ltd
ABN 58 402 937 615
82 Gumleaf Creek Road, Moree NSW 2400

Harold Benton
Managing Director
P 0418 639 204
E haroldbenton@brolgaridgeexc.com.au

Font styles to use
Serif
Sans Serif

Requirements
Nice to have
• I have attached some examples of ideas.
Should not have
• images of machinery

```html
<!DOCTYPE html>
<html lang="en">
<head>
<meta charset="utf-8">
<title>Brolga Ridge Excavations – Business Card</title>
<link rel="stylesheet" href="https://fonts.googleapis.com/css2?family=Montserrat:wght@600;800&family=Roboto:wght@400;500;700&display=swap">
<style>
  :root {
    --orange: #f48a20;
    --charcoal: #222326;
    --logo-grey: #3d3d40;
    --ink: #1a1a1a;
    --paper: #ffffff;
    --backdrop: #3b3c40;
  }
  * { box-sizing: border-box; margin: 0; padding: 0; }
  html, body { width: 1200px; height: 1200px; overflow: hidden; }
  body {
    background: var(--backdrop);
    font-family: "Roboto", Arial, sans-serif;
    position: relative;
  }
  .card {
    position: absolute;
    left: 170px;
    width: 860px;
    height: 500px;
    border-radius: 30px;
    overflow: hidden;
    box-shadow: 0 14px 30px rgba(0,0,0,0.45);
  }
  .card-front { top: 60px; background: var(--orange); }
  .card-back { top: 640px; background: var(--paper); }

  .front-brand {
    position: absolute;
    left: 0; right: 0; top: 130px;
    text-align: center;
    color: var(--paper);
    font-family: "Montserrat", Arial, sans-serif;
    font-weight: 800;
    text-transform: uppercase;
  }
  .front-brand .brand-main { display: block; font-size: 78px; letter-spacing: 2px; line-height: 1; }
  .front-brand .brand-sub { display: block; font-size: 31px; letter-spacing: 3px; margin-top: 14px; }
  .tagline {
    position: absolute;
    left: 0; right: 0; top: 390px;
    text-align: center;
    color: var(--paper);
    font-family: "Montserrat", Arial, sans-serif;
    font-weight: 800;
    font-size: 17px;
    letter-spacing: 1px;
  }

  .back-art { position: absolute; inset: 0; width: 100%; height: 100%; }
  .back-brand {
    position: absolute;
    left: 40px; top: 195px;
    color: var(--logo-grey);
    font-family: "Montserrat", Arial, sans-serif;
    font-weight: 800;
    text-transform: uppercase;
    line-height: 1;
  }
  .back-brand .brand-main { display: block; font-size: 52px; letter-spacing: 1px; }
  .back-brand .brand-sub { display: block; font-size: 21px; letter-spacing: 2px; margin-top: 10px; }

  .contact {
    position: absolute;
    right: 48px; top: 170px;
    text-align: right;
    color: var(--ink);
  }
  .person-name {
    font-family: "Montserrat", Arial, sans-serif;
    font-weight: 800;
    font-size: 32px;
    color: var(--orange);
    text-transform: uppercase;
  }
  .person-role { font-size: 20px; margin-top: 2px; }
  .company-block { margin-top: 38px; font-size: 17px; line-height: 1.4; }
  .company-name { color: var(--orange); font-weight: 500; }
  .contact-lines { margin-top: 16px; font-size: 17px; line-height: 1.6; }
  .contact-line { display: flex; justify-content: flex-end; align-items: center; gap: 10px; }
  .contact-line svg { width: 18px; height: 18px; fill: var(--orange); }
</style>
</head>
<body>

<section class="card card-front" aria-label="Business card front">
  <div class="front-brand">
    <span class="brand-main">Brolga Ridge</span>
    <span class="brand-sub">Excavations Pty Ltd</span>
  </div>
  <p class="tagline">AGRICULTURE &bull; CIVIL CONSTRUCTION &bull; MINING.</p>
</section>

<section class="card card-back" aria-label="Business card back">
  <svg class="back-art" viewBox="0 0 860 500" preserveAspectRatio="none" aria-hidden="true">
    <polygon points="0,0 560,0 370,175 0,175" fill="var(--charcoal)"/>
    <polygon points="560,0 600,0 410,175 370,175" fill="var(--orange)"/>
    <polygon points="0,365 320,365 250,500 0,500" fill="var(--orange)"/>
  </svg>

  <div class="back-brand">
    <span class="brand-main">Brolga Ridge</span>
    <span class="brand-sub">Excavations Pty Ltd</span>
  </div>

  <div class="contact">
    <p class="person-name">Harold Benton</p>
    <p class="person-role">Managing Director</p>
    <div class="company-block">
      <p class="company-name">Brolga Ridge Excavations Pty Ltd</p>
      <p>ABN 58 402 937 615</p>
      <p>82 Gumleaf Creek Road, Moree NSW 2400</p>
    </div>
    <div class="contact-lines">
      <p class="contact-line">0418 639 204
        <svg viewBox="0 0 24 24" aria-label="Phone"><path d="M6.6 10.8a15.1 15.1 0 0 0 6.6 6.6l2.2-2.2a1 1 0 0 1 1-.25 11.4 11.4 0 0 0 3.6.57 1 1 0 0 1 1 1V20a1 1 0 0 1-1 1A17 17 0 0 1 3 4a1 1 0 0 1 1-1h3.5a1 1 0 0 1 1 1c0 1.25.2 2.45.57 3.57a1 1 0 0 1-.25 1z"/></svg>
      </p>
      <p class="contact-line">haroldbenton@brolgaridgeexc.com.au
        <svg viewBox="0 0 24 24" aria-label="Email"><path d="M3 5h18a1 1 0 0 1 1 1v12a1 1 0 0 1-1 1H3a1 1 0 0 1-1-1V6a1 1 0 0 1 1-1zm9 7.2L4 7.4V8l8 4.9L20 8v-.6z"/></svg>
      </p>
    </div>
  </div>
</section>

</body>
</html>
```